Etiketten für Imkerei aus der Steiermark
Zielgruppe
Wir sind eine Imkerei aus der Steiermark / Österreich im Vollerwerb. www.brandl-imker.at
Zielgruppe: Frauen, Familien, Regional
Unser Image: hohe Qualität, Familienbetrieb, naturnah, gesund
Vermarktung: Direkt, Verkaufsstellen, Märkte, zukünftig auch online
Aufgabenstellung
Wir werden die Honiggläser und die Druckerei umstellen und möchten hierfür ein profesionelles abgestimmtes Design. Unser Logo soll erhalten bleiben. Die Honigsortenbezeichnung (Waldhonig, Cremehonig, Blütenhonig) soll zukünftig eingedruckt werden und neben dem Logo ein Zentrales Element sein.
In Zukunft verwenden wir Vorsta Gläser mit hohen Deckel der Firma Plomanta in den Größen 1000g(Lisa 785), 500g (Vor 410), 250 g (Vor 212) und 150 g (Vor 125). Der Deckel soll einheitlich Gold oder Silber sein.

```html
<!DOCTYPE html>
<html lang="de">
<head>
<meta charset="utf-8">
<title>Etiketten Waldhonig – Brandl Imker</title>
<link href="https://fonts.googleapis.com/css2?family=Amatic+SC:wght@700&family=Montserrat:wght@300;400;600;800&family=Roboto+Condensed:wght@400;700&display=swap" rel="stylesheet">
<style>
  :root {
    --bg: #d9d9d9;
    --label: #ffffff;
    --ink: #333333;
    --muted: #6f6f6f;
    --green: #1f7a3a;
    --yellow: #fbf197;
  }
  * { box-sizing: border-box; margin: 0; padding: 0; }
  html, body { width: 1200px; height: 2314px; overflow: hidden; background: var(--bg); }
  .sheet { position: relative; width: 1200px; height: 2314px; }

  .sheet-heading { position: absolute; top: 260px; left: 0; width: 100%; text-align: center; color: var(--muted); }
  .sheet-heading .title { font: 300 34px/1 "Montserrat", sans-serif; letter-spacing: 4px; }
  .sheet-heading .sizes { margin-top: 22px; font: 600 28px/1 "Montserrat", sans-serif; letter-spacing: 1.5px; }

  .label { position: absolute; left: 50%; transform: translateX(-50%); background: var(--label); color: var(--ink); }
  .label--large { top: 440px; width: 875px; height: 630px; }
  .label--medium { top: 1170px; width: 798px; height: 385px; }
  .label--small { top: 1655px; width: 700px; height: 245px; }

  .label-center { position: absolute; left: 0; right: 0; display: flex; flex-direction: column; align-items: center; }
  .variety { font-family: "Amatic SC", cursive; font-weight: 700; line-height: .9; letter-spacing: 1px; }
  .quality-band { background: var(--green); color: #fff; font-family: "Montserrat", sans-serif; font-weight: 400; letter-spacing: 1px; white-space: nowrap; }
  .weight { font-family: "Montserrat", sans-serif; font-weight: 600; }
  .brand { display: flex; flex-direction: column; align-items: center; }
  .brand-dot { border-radius: 50%; background: var(--yellow); border: 0; }
  .brand-name { font-family: "Montserrat", sans-serif; font-weight: 800; color: var(--ink); text-align: center; line-height: 1; }
  .website { font-family: "Roboto Condensed", sans-serif; font-weight: 700; color: var(--ink); }

  .contact, .storage { position: absolute; font-family: "Roboto Condensed", sans-serif; color: var(--muted); line-height: 1.3; }
  .storage { text-align: right; }
  .storage .best-before { display: block; font-weight: 700; color: var(--ink); }

  /* large 125 x 90 mm */
  .label--large .label-center { top: 55px; }
  .label--large .variety { font-size: 96px; }
  .label--large .quality-band { margin-top: 10px; padding: 6px 16px; font-size: 24px; }
  .label--large .weight { margin-top: 12px; font-size: 24px; }
  .label--large .brand { margin-top: 50px; }
  .label--large .brand-dot { width: 46px; height: 46px; margin-bottom: 14px; }
  .label--large .brand-name { font-size: 50px; }
  .label--large .website { position: absolute; top: 585px; left: 0; right: 0; text-align: center; font-size: 16px; }
  .label--large .contact { left: 34px; top: 510px; font-size: 15px; }
  .label--large .storage { right: 34px; top: 510px; font-size: 15px; }
  .label--large .storage .best-before { margin-top: 12px; }

  /* medium 114 x 55 mm */
  .label--medium .label-center { top: 35px; }
  .label--medium .variety { font-size: 68px; }
  .label--medium .quality-band { margin-top: 6px; padding: 4px 14px; font-size: 18px; }
  .label--medium .weight { margin-top: 10px; font-size: 18px; }
  .label--medium .brand { margin-top: 26px; }
  .label--medium .brand-dot { width: 28px; height: 28px; margin-bottom: 8px; }
  .label--medium .brand-name { font-size: 32px; }
  .label--medium .website { position: absolute; top: 345px; left: 0; right: 0; text-align: center; font-size: 15px; }
  .label--medium .contact { left: 30px; top: 272px; font-size: 14px; }
  .label--medium .storage { right: 30px; top: 272px; font-size: 14px; }
  .label--medium .storage .best-before { margin-top: 10px; }

  /* small 100 x 35 mm */
  .label--small .label-center { top: 20px; }
  .label--small .variety { font-size: 54px; }
  .label--small .quality-band { margin-top: 4px; padding: 3px 12px; font-size: 15px; }
  .label--small .brand { margin-top: 16px; }
  .label--small .brand-dot { width: 20px; height: 20px; margin-bottom: 6px; }
  .label--small .brand-name { font-size: 24px; }
  .label--small .weight-corner { position: absolute; top: 20px; right: 20px; font-size: 15px; }
  .label--small .website { position: absolute; top: 212px; left: 0; right: 0; text-align: center; font-size: 14px; }
  .label--small .contact { left: 20px; top: 140px; font-size: 13px; }
  .label--small .storage { right: 20px; top: 140px; font-size: 13px; }
  .label--small .storage .best-before { margin-top: 8px; }
</style>
</head>
<body>
<main class="sheet">
  <header class="sheet-heading">
    <p class="title">ETIKETTEN</p>
    <p class="sizes">125 x 90 mm · 114 x 55 mm · 100 x 35 mm</p>
  </header>

  <section class="label label--large">
    <div class="label-center">
      <h1 class="variety">WALDHONIG</h1>
      <p class="quality-band">Österreichischer Qualitätshonig</p>
      <p class="weight">150g</p>
      <div class="brand"><span class="brand-dot"></span><span class="brand-name">Brandl<br>Imker</span></div>
    </div>
    <p class="contact">Meisterimkerei Brandl<br>Birkenweg 12<br>8160 Almtal<br>Tel: 0664 /55 01 234<br>brandl-imker@mailpost.at</p>
    <p class="storage">Trocken und vor Wärme<br>geschützt lagern!<span class="best-before">Mindestens haltbar bis:</span></p>
    <p class="website">www.brandl-imker.at</p>
  </section>

  <section class="label label--medium">
    <div class="label-center">
      <h2 class="variety">WALDHONIG</h2>
      <p class="quality-band">Österreichischer Qualitätshonig</p>
      <p class="weight">150g</p>
      <div class="brand"><span class="brand-dot"></span><span class="brand-name">Brandl<br>Imker</span></div>
    </div>
    <p class="contact">Meisterimkerei Brandl<br>Birkenweg 12<br>8160 Almtal<br>Tel: 0664 /55 01 234<br>brandl-imker@mailpost.at</p>
    <p class="storage">Trocken und vor Wärme<br>geschützt lagern!<span class="best-before">Mindestens haltbar bis:</span></p>
    <p class="website">www.brandl-imker.at</p>
  </section>

  <section class="label label--small">
    <div class="label-center">
      <h2 class="variety">WALDHONIG</h2>
      <p class="quality-band">Österreichischer Qualitätshonig</p>
      <div class="brand"><span class="brand-dot"></span><span class="brand-name">Brandl Imker</span></div>
    </div>
    <p class="weight weight-corner">150g</p>
    <p class="contact">Meisterimkerei Brandl<br>Birkenweg 12<br>8160 Almtal<br>Tel: 0664 /55 01 234<br>brandl-imker@mailpost.at</p>
    <p class="storage">Trocken und vor Wärme<br>geschützt lagern!<span class="best-before">Mindestens haltbar bis:</span></p>
    <p class="website">www.brandl-imker.at</p>
  </section>
</main>
</body>
</html>
```